Christmas Collection Candle Label Design

Looking to update our existing Christmas Candle Collection labels. Labels should reflect the overall feel of our brand- www.kelvabrite.ca
Want to include some color elements. Holiday colors added into design but more muted/ earthy tones not vibrant colors . Metallic elements and line art botanical illustration. Fonts should be more align to brand
Scents
Winter Lantern
Frost Berry
Amber and Fig
Belle Étoile

```html
<!DOCTYPE html>
<html lang="en">
<head>
<meta charset="utf-8">
<title>Kelvabrite Christmas Collection Labels</title>
<link rel="stylesheet" href="https://fonts.googleapis.com/css2?family=Playfair+Display:wght@400&family=Libre+Baskerville&display=swap">
<style>
  :root {
    --bg-top: #aeaeae;
    --bg-bottom: #d2bba8;
    --paper: #ffffff;
    --ink-light: #f4f1ec;
    --ink-dark: #3a2a1a;
    --pine: #548a4f;
    --berry: #c05a5f;
    --amber: #c1785c;
    --frost: #5a8ec0;
    --gold-1: #d99a22;
    --gold-2: #f3d86a;
    --gold-3: #e0a834;
    --chip-1: #e8c169;
    --chip-2: #f3dca0;
    --chip-3: #e6b75a;
    --chip-4: #f2e6c8;
  }
  * { margin: 0; padding: 0; box-sizing: border-box; }
  html, body { width: 1173px; height: 1200px; overflow: hidden; }
  body {
    background: linear-gradient(180deg, var(--bg-top), var(--bg-bottom));
    position: relative;
  }
  .label {
    position: absolute;
    width: 487px; height: 487px;
    background: var(--paper);
    padding: 10px;
    box-shadow: 0 14px 28px rgba(60, 40, 20, 0.28);
  }
  .label--pine { left: 76px; top: 74px; --tone: var(--pine); }
  .label--berry { left: 606px; top: 74px; --tone: var(--berry); }
  .label--amber { left: 76px; top: 611px; --tone: var(--amber); }
  .label--frost { left: 606px; top: 611px; --tone: var(--frost); }

  .label__face {
    position: relative;
    width: 100%; height: 100%;
    background: var(--tone);
    overflow: hidden;
  }
  .label__art {
    position: absolute; inset: 0;
    background:
      radial-gradient(circle at 20% 22%, rgba(255,255,255,0.16), transparent 30%),
      radial-gradient(circle at 85% 80%, rgba(255,255,255,0.14), transparent 32%),
      radial-gradient(circle at 50% 75%, rgba(255,255,255,0.10), transparent 28%);
  }
  .label__frame {
    position: absolute;
    left: 11px; top: 11px; right: 11px; bottom: 11px;
    border: 3px solid;
    border-image: linear-gradient(180deg, var(--gold-1), var(--gold-2) 30%, var(--gold-3) 55%, var(--gold-2) 80%, var(--gold-1)) 1;
  }
  .brand {
    position: absolute; left: 0; right: 0; top: 50px;
    text-align: center;
    font-family: "Playfair Display", serif;
    font-size: 15px; letter-spacing: 1px;
    color: var(--ink-light);
  }
  .title {
    position: absolute; left: 0; right: 0; top: 130px;
    text-align: center;
    font-family: "Playfair Display", serif;
    font-weight: 400;
    font-size: 66px; line-height: 68px;
    color: var(--ink-light);
    text-transform: uppercase;
  }
  .title__small { font-size: 40px; }
  .est, .year {
    position: absolute; top: 290px;
    font-family: "Playfair Display", serif;
    font-size: 28px; letter-spacing: 1px;
    color: var(--ink-light);
  }
  .est { left: 76px; }
  .year { right: 61px; }
  .chip {
    position: absolute; top: 394px; height: 47px;
    display: flex; align-items: center; justify-content: center;
    text-align: center;
    font-family: "Libre Baskerville", serif;
    font-size: 11.5px; line-height: 12px;
    color: var(--ink-dark);
    background: linear-gradient(100deg, var(--chip-1), var(--chip-2) 45%, var(--chip-3) 75%, var(--chip-4));
  }
  .chip--origin { left: 23px; width: 132px; }
  .chip--oil { left: 160px; width: 145px; }
  .chip--weight { left: 310px; width: 135px; }
</style>
</head>
<body>

<section class="label label--pine">
  <div class="label__face">
    <div class="label__art" role="img" aria-label="Faint line-art botanicals: holly, pine cone and leafy branches"></div>
    <div class="label__frame"></div>
    <div class="brand">KELVABRITE</div>
    <h2 class="title">Winter<br>Lantern</h2>
    <span class="est">EST</span><span class="year">2005</span>
    <div class="chip chip--origin">Marketplace<br>connection</div>
    <div class="chip chip--oil">Made with pure<br>essential oil</div>
    <div class="chip chip--weight">Net weight: 120g</div>
  </div>
</section>

<section class="label label--berry">
  <div class="label__face">
    <div class="label__art" role="img" aria-label="Faint line-art candy canes, holly and bows"></div>
    <div class="label__frame"></div>
    <div class="brand">KELVABRITE</div>
    <h2 class="title">Frost<br>Berry</h2>
    <span class="est">EST</span><span class="year">2005</span>
    <div class="chip chip--origin">Marketplace<br>connection</div>
    <div class="chip chip--oil">Made with pure<br>essential oil</div>
    <div class="chip chip--weight">Net weight: 120g</div>
  </div>
</section>

<section class="label label--amber">
  <div class="label__face">
    <div class="label__art" role="img" aria-label="Faint line-art spices, leaves, peppers, star anise and wrapped sweets"></div>
    <div class="label__frame"></div>
    <div class="brand">KELVABRITE</div>
    <h2 class="title">Amber <span class="title__small">and</span><br>Fig</h2>
    <span class="est">EST</span><span class="year">2005</span>
    <div class="chip chip--origin">Marketplace<br>connection</div>
    <div class="chip chip--oil">Made with pure<br>essential oil</div>
    <div class="chip chip--weight">Net weight: 120g</div>
  </div>
</section>

<section class="label label--frost">
  <div class="label__face">
    <div class="label__art" role="img" aria-label="Faint line-art snowflakes, holly berries, bells and poinsettia"></div>
    <div class="label__frame"></div>
    <div class="brand">KELVABRITE</div>
    <h2 class="title">Belle<br>Étoile</h2>
    <span class="est">EST</span><span class="year">2005</span>
    <div class="chip chip--origin">Marketplace<br>connection</div>
    <div class="chip chip--oil">Made with pure<br>essential oil</div>
    <div class="chip chip--weight">Net weight: 120g</div>
  </div>
</section>

</body>
</html>
```